Lantern Advisory Business Cards

We need a new layout for our business cards. We have a logo already. But we might be interested in only using the Lantern portion of the logo. It has been uploaded.

We would like cards that are not overly busy. Clean. Modern. Perhaps a gray color for one side.

On the back, we would like to have the lantern part of the logo and "Take the Leap, we've got you!"

Our business provides medics and safety training for corporate clients. Our website is www.lanternadvisoryllc.example.

Industry/Entity Type

Business

Contact Information for Business Card

We want include name, email address, cell phone, main line number, and website URL on the front. Use the following as an example: Marla Tobin, marla@lanternadvisoryllc.example, 402.318.7264 (cell), 402.947.315, and www.lanternadvisoryllc.example.

Font styles to use
Serif
Sans Serif

Requirements
Must have
• All required information. Back side logo with "Take the leap, we will catch you!"
Nice to have
• If possible, we would like to consider creating a card in a non-standard shape. Perhaps, the shape of a lantern. Just interested in understanding the option.

```html
<!DOCTYPE html>
<html lang="en">
<head>
<meta charset="utf-8">
<title>Lantern Advisory — Business Cards</title>
<link href="https://fonts.googleapis.com/css2?family=Open+Sans:ital,wght@0,400;0,600;0,700;1,400&display=swap" rel="stylesheet">
<style>
  :root {
    --backdrop: #d9d6d1;
    --card-white: #ffffff;
    --card-gray: #e3e5e3;
    --brand-blue: #2a4f86;
    --ink: #3a3a3a;
    --ink-soft: #555555;
    --rule: #9a9a9a;
  }
  * { box-sizing: border-box; margin: 0; padding: 0; }
  html, body { width: 1200px; height: 843px; overflow: hidden; }
  body {
    background: var(--backdrop);
    font-family: "Open Sans", Arial, sans-serif;
    position: relative;
  }
  .card {
    position: absolute;
    top: 278px;
    width: 500px;
    height: 286px;
    border-radius: 4px;
    box-shadow: 0 0 0 3px var(--brand-blue), 0 10px 24px rgba(0,0,0,.25);
    overflow: hidden;
  }
  /* Back side */
  .card-back { left: 50px; background: var(--card-gray); }
  .back-mark {
    position: absolute;
    top: 58px; left: 250px;
    display: flex; align-items: center; gap: 10px;
    color: var(--brand-blue);
    font-weight: 600; font-size: 17px; letter-spacing: .5px;
  }
  .back-mark .dot { width: 22px; height: 22px; border-radius: 50%; background: var(--brand-blue); }
  .back-tagline {
    position: absolute;
    left: 40px; bottom: 70px;
    color: var(--brand-blue);
    font-style: italic;
    font-size: 23px;
  }
  /* Front side */
  .card-front { left: 650px; background: var(--card-white); }
  .front-logo {
    position: absolute;
    top: 42px; right: 34px;
    text-align: right;
  }
  .front-logo .wordmark {
    display: flex; align-items: center; justify-content: flex-end; gap: 10px;
    font-weight: 600; font-size: 24px; color: var(--ink); letter-spacing: 1px;
  }
  .front-logo .dot { width: 18px; height: 18px; border-radius: 50%; background: var(--brand-blue); }
  .front-logo .motto {
    margin-top: 2px;
    font-size: 9px; letter-spacing: 3.2px; text-transform: uppercase; color: var(--ink-soft);
  }
  .holder-name {
    position: absolute;
    top: 112px; left: 34px;
    font-weight: 700; font-size: 21px; color: var(--ink-soft);
  }
  .divider {
    position: absolute;
    left: 236px; top: 128px;
    width: 1px; height: 90px;
    background: var(--rule);
  }
  .contact-list {
    position: absolute;
    left: 254px; top: 136px;
    list-style: none;
  }
  .contact-list li {
    display: flex; align-items: center; gap: 10px;
    font-size: 13px; color: var(--ink); line-height: 1; margin-bottom: 9px;
  }
  .contact-list svg { width: 15px; height: 15px; fill: var(--ink-soft); flex: none; }
</style>
</head>
<body>

  <section class="card card-back" aria-label="Card back">
    <div class="back-mark"><span class="dot"></span>Lantern Advisory</div>
    <p class="back-tagline">Take the leap,&nbsp; we will catch you!</p>
  </section>

  <section class="card card-front" aria-label="Card front">
    <div class="front-logo">
      <div class="wordmark">Lantern Advisory<span class="dot"></span></div>
      <div class="motto">The preparedness people</div>
    </div>

    <h1 class="holder-name">Marla Tobin</h1>
    <div class="divider"></div>

    <ul class="contact-list">
      <li>
        <svg viewBox="0 0 16 16" aria-hidden="true"><path d="M3.5 1.5l2.5 0 1 3.5-1.7 1.2a9 9 0 0 0 4.5 4.5L11 9l3.5 1v2.5c0 1-1 2-2 2A11 11 0 0 1 1.5 3.5c0-1 1-2 2-2z"/></svg>
        402 318 7264
      </li>
      <li>
        <svg viewBox="0 0 16 16" aria-hidden="true"><path d="M4 1h8a1 1 0 0 1 1 1v12a1 1 0 0 1-1 1H4a1 1 0 0 1-1-1V2a1 1 0 0 1 1-1zm1 2v8h6V3zm3 9.2a.9.9 0 1 0 0 1.8.9.9 0 0 0 0-1.8z"/></svg>
        402 947 315
      </li>
      <li>
        <svg viewBox="0 0 16 16" aria-hidden="true"><path d="M1 4h14v9H1zm1.2 1L8 9.3 13.8 5z"/></svg>
        marla@lanternadvisoryllc.example
      </li>
      <li>
        <svg viewBox="0 0 16 16" aria-hidden="true"><path d="M8 1a7 7 0 1 0 0 14A7 7 0 0 0 8 1zm0 1.4c.8 0 1.7 1.6 2 4H6c.3-2.4 1.2-4 2-4zM2.5 7.4h2.3a13 13 0 0 0 0 1.2H2.5zm3.5 1.2h4c-.3 2.4-1.2 4-2 4s-1.7-1.6-2-4zm5.2-1.2h2.3v1.2h-2.3a13 13 0 0 0 0-1.2z"/></svg>
        www.lanternadvisoryllc.example
      </li>
    </ul>
  </section>

</body>
</html>
```